Regional Consulting Business Needs a Business Card Design

We need a business card design for our new business based in Regional Victoria, Australia called Brindle Power. We are a consulting company with our main goal being to save people momey money and reducing their carbon footprint. Anything from water saving showerheads, to energy saving lightglobes and even to solar power. We would like to see designs that use bright colours. The final design should shout 'we are here to help you'.

Industry/Entity Type

Business

```html
<!DOCTYPE html>
<html lang="en">
<head>
<meta charset="utf-8">
<title>Brindle Power – Business Card</title>
<link href="https://fonts.googleapis.com/css2?family=Arimo:ital,wght@0,400;0,700;1,400&display=swap" rel="stylesheet">
<style>
  :root {
    --backdrop: #d9d9d9;
    --card-white: #ffffff;
    --card-cream: #f3f2ee;
    --orange: #f39a1e;
    --orange-light: #fbc02d;
    --orange-deep: #e8891a;
    --charcoal: #2e2e2e;
    --grey-mid: #6d6d6d;
    --grey-light: #b5b5b5;
    --name-white: #fff6e6;
  }
  * { box-sizing: border-box; margin: 0; padding: 0; }
  html, body {
    width: 1200px; height: 900px; overflow: hidden;
    background: var(--backdrop);
    font-family: "Arimo", Arial, sans-serif;
  }
  .canvas { position: relative; width: 1200px; height: 900px; }

  .card {
    position: absolute; width: 640px; height: 366px;
    border-radius: 26px; overflow: hidden;
    box-shadow: 0 6px 18px rgba(0,0,0,.25);
  }

  /* Back of card */
  .card-back { left: 470px; top: 50px; background: var(--card-white); }
  .card-back .brand { position: absolute; left: 120px; top: 140px; }
  .card-back .site { position: absolute; right: 40px; bottom: 40px; font-size: 17px; color: var(--charcoal); }

  .brand { display: flex; flex-direction: column; }
  .brand-row { display: flex; align-items: center; gap: 12px; }
  .brand-square { width: 34px; height: 34px; background: var(--orange); }
  .brand-name { font-size: 38px; font-weight: 700; color: var(--charcoal); line-height: 1; }
  .brand-tagline { margin: 6px 0 0 46px; font-size: 14px; font-style: italic; color: var(--charcoal); }

  /* Front of card */
  .card-front { left: 90px; top: 480px; background: linear-gradient(160deg, #ffffff 0%, var(--card-cream) 60%, #e9e7e1 100%); }
  .card-front .swoosh { position: absolute; inset: 0; width: 100%; height: 100%; }
  .card-front .brand { position: absolute; left: 40px; top: 104px; }
  .card-front .brand-name { font-size: 34px; }
  .card-front .brand-square { width: 30px; height: 30px; }
  .card-front .brand-tagline { font-size: 13px; margin-left: 42px; }

  .person { position: absolute; left: 404px; top: 58px; }
  .person-name { font-size: 28px; color: var(--charcoal); line-height: 1.1; }
  .person-name b { font-weight: 700; }
  .person-role { margin-top: 4px; font-size: 14px; letter-spacing: .5px; color: var(--name-white); }

  .address { position: absolute; left: 40px; top: 238px; font-size: 19px; line-height: 1.25; color: var(--charcoal); }
  .divider { position: absolute; left: 318px; top: 232px; width: 2px; height: 100px; background: var(--charcoal); }

  .contacts { position: absolute; left: 334px; top: 230px; list-style: none; }
  .contacts li { display: flex; align-items: center; gap: 14px; height: 26px; font-size: 18px; color: var(--charcoal); }
  .contacts svg { width: 16px; height: 16px; flex: none; }
</style>
</head>
<body>
<main class="canvas">

  <section class="card card-back">
    <div class="brand">
      <div class="brand-row">
        <span class="brand-square"></span>
        <span class="brand-name">Brindle Power</span>
      </div>
      <span class="brand-tagline">Maintenence and consulting services</span>
    </div>
    <span class="site">www.brindlepower.com</span>
  </section>

  <section class="card card-front">
    <svg class="swoosh" viewBox="0 0 640 366" preserveAspectRatio="none" aria-hidden="true">
      <defs>
        <linearGradient id="band" x1="0" y1="0" x2="1" y2="0">
          <stop offset="0" stop-color="var(--orange)"/>
          <stop offset=".45" stop-color="var(--orange-light)"/>
          <stop offset=".7" stop-color="var(--orange)"/>
          <stop offset="1" stop-color="var(--orange-deep)"/>
        </linearGradient>
      </defs>
      <path d="M0,0 H640 V196 C540,194 450,180 380,124 C300,46 160,22 0,28 Z" fill="url(#band)"/>
      <path d="M0,36 C160,24 300,48 380,128 C450,190 540,204 640,204" fill="none" stroke="var(--grey-light)" stroke-width="4"/>
      <path d="M0,46 C160,34 300,60 380,140 C450,200 540,214 640,216" fill="none" stroke="var(--charcoal)" stroke-width="6"/>
    </svg>

    <div class="brand">
      <div class="brand-row">
        <span class="brand-square"></span>
        <span class="brand-name">Brindle Power</span>
      </div>
      <span class="brand-tagline">Maintenence and consulting services</span>
    </div>

    <div class="person">
      <p class="person-name"><b>Dana</b> Whitlock</p>
      <p class="person-role">GENERAL MANAGER</p>
    </div>

    <p class="address">Level 2, 48 Ridgeway St.<br>Bendigo East, Victoria 3550</p>
    <span class="divider"></span>

    <ul class="contacts">
      <li>
        <svg viewBox="0 0 16 16"><path d="M2 6 C2 3 14 3 14 6 L11 7 L10 5 H6 L5 7 Z M4 8 H12 L13 13 H3 Z" fill="var(--orange)"/></svg>
        +61 3 5550 0142
      </li>
      <li>
        <svg viewBox="0 0 16 16"><rect x="2" y="4" width="12" height="10" rx="2" fill="var(--orange)"/><rect x="5" y="1" width="6" height="5" fill="var(--orange)" stroke="#fff" stroke-width="1"/><rect x="5" y="8" width="6" height="3" fill="#fff"/></svg>
        +61 3 5550 0187
      </li>
      <li>
        <svg viewBox="0 0 16 16"><rect x="1" y="4" width="14" height="9" fill="var(--orange)"/><path d="M1 4 L8 9 L15 4" fill="none" stroke="#fff" stroke-width="1.2"/></svg>
        info@brindlepower.com
      </li>
      <li>
        <svg viewBox="0 0 16 16"><circle cx="8" cy="8" r="6.5" fill="var(--orange)"/><path d="M1.5 8 H14.5 M8 1.5 V14.5 M8 1.5 C4 5 4 11 8 14.5 M8 1.5 C12 5 12 11 8 14.5" fill="none" stroke="#fff" stroke-width=".9"/></svg>
        www.brindlepower.com
      </li>
    </ul>
  </section>

</main>
</body>
</html>
```